Corporate Template

Looking for a set of corporate slides to be made which contain multiple different slides and orientations. Looking for at least 8 to 10 different master pages plus a Coversheet and closeout page. Incorporating a color palate similar to our logo coloring is preferred.

I have attached a logo.

```html
<!DOCTYPE html>
<html lang="en">
<head>
<meta charset="UTF-8">
<title>Business Presentation – Cover Slide</title>
<link href="https://fonts.googleapis.com/css2?family=Bebas+Neue&family=Lato:wght@400;700&display=swap" rel="stylesheet">
<style>
  :root {
    --brand-blue: #2f9bd8;
    --ink: #111111;
    --text-grey: #7a7a7a;
    --link-grey: #555555;
    --icon-grey: #9a9a9a;
    --control-grey: #666666;
    --bar-grey: #f2f2f2;
    --line-grey: #dcdcdc;
    --page: #ffffff;
    --photo-light: #eef1f5;
    --photo-mid: #c9d3de;
    --photo-dark: #8b9bb0;
  }
  * { margin: 0; padding: 0; box-sizing: border-box; }
  html, body { width: 1200px; height: 800px; overflow: hidden; background: var(--page); }
  .slide {
    position: relative;
    width: 1200px;
    height: 800px;
    background: var(--page);
    font-family: "Lato", sans-serif;
  }
  .hero-photo {
    position: absolute;
    left: 38px;
    top: 252px;
    width: 450px;
    height: 206px;
    background: linear-gradient(110deg, var(--photo-mid) 0%, var(--photo-light) 35%, var(--photo-light) 60%, var(--photo-mid) 85%, var(--photo-dark) 100%);
  }
  .hero-brand {
    position: absolute;
    left: 152px;
    top: 278px;
    display: flex;
    align-items: center;
    gap: 8px;
    font-weight: 700;
    font-size: 24px;
    color: var(--brand-blue);
    letter-spacing: 0.5px;
  }
  .brand-square {
    width: 22px;
    height: 22px;
    background: var(--brand-blue);
  }
  .title {
    position: absolute;
    left: 510px;
    top: 280px;
    font-family: "Bebas Neue", sans-serif;
    font-weight: 400;
    font-size: 86px;
    line-height: 0.88;
    letter-spacing: 1px;
  }
  .title span { display: block; }
  .title .accent { color: var(--brand-blue); }
  .title .dark { color: var(--ink); }
  .intro {
    position: absolute;
    left: 488px;
    top: 522px;
    width: 520px;
    font-size: 12.5px;
    line-height: 1.6;
    color: var(--text-grey);
  }
  .nav-bar {
    position: absolute;
    left: 0;
    top: 652px;
    width: 1200px;
    height: 36px;
    background: var(--bar-grey);
    border-top: 1px solid var(--line-grey);
    border-bottom: 1px solid var(--line-grey);
  }
  .slide-controls {
    position: absolute;
    left: 22px;
    top: 8px;
  }
  .social-links {
    position: absolute;
    left: 182px;
    top: 0;
    height: 34px;
    display: flex;
    align-items: center;
    list-style: none;
    font-size: 12px;
    color: var(--link-grey);
  }
  .social-links li { display: flex; align-items: center; gap: 10px; width: 162px; }
  .social-dot {
    width: 15px;
    height: 15px;
    border-radius: 50%;
    background: var(--icon-grey);
  }
  .footer-brand {
    position: absolute;
    right: 60px;
    top: 756px;
    display: flex;
    align-items: center;
    gap: 6px;
    font-weight: 700;
    font-size: 15px;
    color: var(--brand-blue);
  }
  .footer-brand .brand-square { width: 14px; height: 14px; }
</style>
</head>
<body>
<main class="slide">
  <div class="hero-photo" role="img" aria-label="Photo of business people reviewing charts on a tablet and printed reports at a desk"></div>
  <div class="hero-brand"><span class="brand-square"></span>NORTHWARD CO</div>

  <h1 class="title">
    <span class="accent">Business</span>
    <span class="dark">Slidedeck</span>
    <span class="accent">Presentation</span>
  </h1>

  <p class="intro">Lorem Ipsum is simply dummy text of the printing and typesetting industry. Lorem Ipsum has been the industry's standard dummy text ever since the 1500s, when an unknown printer took a galley of type and scrambled it to make a type specimen book.</p>

  <nav class="nav-bar">
    <svg class="slide-controls" width="64" height="18" viewBox="0 0 64 18" aria-label="Slide navigation">
      <circle cx="9" cy="9" r="7.5" fill="none" stroke="#666" stroke-width="1.2"/>
      <path d="M10.5 5.5 L7 9 L10.5 12.5" fill="none" stroke="#666" stroke-width="1.4"/>
      <rect x="25" y="4" width="10" height="10" fill="none" stroke="#666" stroke-width="1.2"/>
      <circle cx="53" cy="9" r="7.5" fill="none" stroke="#666" stroke-width="1.2"/>
      <path d="M51.5 5.5 L55 9 L51.5 12.5" fill="none" stroke="#666" stroke-width="1.4"/>
    </svg>
    <ul class="social-links">
      <li><span class="social-dot"></span>follow/northwardco</li>
      <li><span class="social-dot"></span>network/northwardco</li>
      <li><span class="social-dot"></span>updates/northwardco</li>
      <li><span class="social-dot"></span>search/northwardco</li>
    </ul>
  </nav>

  <div class="footer-brand"><span class="brand-square"></span>NORTHWARD CO</div>
</main>
</body>
</html>
```